Crestwell Renewal Business Card Design Phase 2

Professional and clean design. The design colors should flow with the logo. Two-sided card with the website on the back which is:

www.CrestwellRenewal.example.

"Specializing in Water Damage Restoration"

On the front I need the name, email, phone, and logo.

Name: Dorian Halvek
Email: Dorian@CrestwellRenewal.example
Phone: 555-318-2046 for now

I only have the Preview and Thumbnail right now but should have the source files uploaded within a day or two.

Target Market(s)

Flood victims, home owners with water damage from busted pipes etc...

Industry/Entity Type

Business

Contact Information for Business Card

Name: Dorian Halvek

Font styles to use
Serif
Sans Serif

Requirements
Must have
• Business Card Details Info

```html
<!DOCTYPE html>
<html lang="en">
<head>
<meta charset="utf-8">
<title>Crestwell Renewal Business Card</title>
<link rel="stylesheet" href="https://fonts.googleapis.com/css2?family=Oswald:wght@500&family=Roboto:wght@400;900&family=Roboto+Condensed:wght@400;700&display=swap">
<style>
  :root {
    --backdrop: #d8d8d8;
    --card-stock: #f1f1ef;
    --navy: #1d3461;
    --leaf-green: #4a873b;
    --bright-green: #0a8e4a;
    --name-green: #139249;
    --ink: #141414;
    --muted-ink: #4a4a4a;
    --panel-text: #eaf5ee;
    --rule: rgba(255, 255, 255, 0.45);
  }
  * { box-sizing: border-box; margin: 0; padding: 0; }
  html, body { width: 1200px; height: 904px; overflow: hidden; }
  body {
    background: var(--backdrop);
    display: flex;
    align-items: center;
    justify-content: center;
    gap: 40px;
    font-family: "Roboto", Arial, sans-serif;
  }
  .card {
    position: relative;
    width: 540px;
    height: 309px;
    background: var(--card-stock);
    box-shadow: 0 6px 18px rgba(0, 0, 0, 0.18);
    overflow: hidden;
  }

  /* Front side: name and contact panel */
  .holder-name {
    position: absolute;
    left: 30px;
    top: 92px;
    font-family: "Roboto", Arial, sans-serif;
    font-weight: 900;
    font-size: 27px;
    line-height: 1.05;
    letter-spacing: 0.5px;
    text-transform: uppercase;
    color: var(--name-green);
  }
  .contact-panel {
    position: absolute;
    left: 205px;
    top: 52px;
    width: 305px;
    height: 205px;
    background: var(--bright-green);
    padding: 34px 20px 0 22px;
  }
  .contact-row {
    display: flex;
    align-items: center;
    gap: 16px;
    height: 48px;
    color: var(--panel-text);
    font-size: 13.5px;
    letter-spacing: 0.3px;
  }
  .contact-row + .contact-row { margin-top: 16px; }
  .contact-icon {
    flex: none;
    width: 24px;
    height: 24px;
  }
  .contact-text {
    flex: 1;
    border-bottom: 1px solid var(--rule);
    padding-bottom: 12px;
    margin-top: 12px;
  }

  /* Back side: wordmark, web address, tagline */
  .wordmark {
    position: absolute;
    left: 34px;
    top: 34px;
    width: 400px;
    text-align: center;
    font-family: "Oswald", "Arial Narrow", sans-serif;
    font-weight: 500;
    font-size: 60px;
    line-height: 1;
    text-transform: uppercase;
    color: var(--navy);
  }
  .wordmark span { display: block; }
  .wordmark span + span { margin-top: 6px; }
  .web-address {
    position: absolute;
    left: 34px;
    top: 196px;
    width: 400px;
    text-align: center;
    font-family: "Roboto Condensed", "Arial Narrow", sans-serif;
    font-size: 15px;
    color: var(--muted-ink);
  }
  .tagline {
    position: absolute;
    left: 24px;
    top: 220px;
    width: 420px;
    text-align: center;
    font-family: "Roboto Condensed", "Arial Narrow", sans-serif;
    font-weight: 700;
    font-size: 18px;
    color: var(--ink);
  }
  .tab-strip {
    position: absolute;
    right: 0;
    top: 0;
    width: 82px;
    height: 100%;
    display: flex;
    flex-direction: column;
    gap: 4px;
    padding: 4px 0 0 0;
  }
  .tab {
    flex: 1;
    background: var(--leaf-green);
    border-radius: 8px 0 0 8px;
  }
</style>
</head>
<body>

  <section class="card card-front" aria-label="Card front">
    <h1 class="holder-name">Dorian<br>Halvek</h1>
    <div class="contact-panel">
      <div class="contact-row">
        <svg class="contact-icon" viewBox="0 0 24 24" aria-hidden="true">
          <rect x="1" y="1" width="22" height="22" rx="5" fill="none" stroke="#eaf5ee" stroke-width="1.5"/>
          <path d="M8 6.5c-.8 0-1.5.7-1.4 1.6.4 4.6 4.7 9 9.3 9.3.9.1 1.6-.6 1.6-1.4v-1.4l-2.4-1-1.2 1.2c-1.6-.8-2.9-2.1-3.7-3.7l1.2-1.2-1-2.4z" fill="#eaf5ee"/>
        </svg>
        <span class="contact-text">555-318-2046</span>
      </div>
      <div class="contact-row">
        <svg class="contact-icon" viewBox="0 0 24 24" aria-hidden="true">
          <rect x="1" y="1" width="22" height="22" rx="5" fill="none" stroke="#eaf5ee" stroke-width="1.5"/>
          <rect x="5.5" y="7.5" width="13" height="9" fill="none" stroke="#eaf5ee" stroke-width="1.4"/>
          <path d="M5.5 7.5l6.5 5 6.5-5" fill="none" stroke="#eaf5ee" stroke-width="1.4"/>
        </svg>
        <span class="contact-text">Dorian@CrestwellRenewal.example</span>
      </div>
    </div>
  </section>

  <section class="card card-back" aria-label="Card back">
    <h2 class="wordmark"><span>Crestwell</span><span>Renewal</span></h2>
    <p class="web-address">www.CrestwellRenewal.example.</p>
    <p class="tagline">"Specializing in Water Damage Restoration"</p>
    <div class="tab-strip" aria-hidden="true">
      <div class="tab"></div>
      <div class="tab"></div>
      <div class="tab"></div>
    </div>
  </section>

</body>
</html>
```